Tavla App Design Project

Tavla Menu/Entertainment application. We are seeking a new design for our "Brevlo" concept

What is “Brevlo?”
*Brevlo interactive software is hosted by an Quorra Tavla 2, which is secured in a custom enclosure for each table or bar counter space in your restaurant.

*Brevlo is an easy to implement interactive menu platform that is a one, two, three plug and play concept.

*Brevlo software features your menu, specials, dishes that you wish to premier, and something for the thirsty customer to see visually through color, movement and suggestion. This can be changed daily with little to no effort.

* Brevlo software currently offers games, controlled and specific websites, and social media programs to ease the wait time of customers; while create a more relaxing experience. Whether it is help for parents or time management for professionals; imagine yourself being able to catch up friends, family and colleagues while viewing today’s current events at your table.

*Brevlo offers much more, with supporting multiple interactive photos and video, promoting upcoming events and new menus items and reasons to return. Our simple search tools for the guests can be updated within seconds for daily or last minute changes to the menu, therefore saving on printing costs avoiding frustration for the servers and guests.

* Software customization: Listed below are some custom features that you may consider to assist you in enriching the dining experience and expanding your customer base.
Linkora, Chirpex and nine pt
Interactive games where guests can compete against one another
Table to Table chat feature to encourage interaction between customers and across locations
Soliciting customer e-mails for special offers or rewards programs
Cross-linking to specific websites that relate to the restaurant and guests
Loyalty Programs and email database growth

photos of current design posted for 1 client. Seeking new design using same functions

Target Market(s)

18 yrs to 55

Industry/Entity Type

Restaurant

Requirements
Must have
• Here is the focus for our application
1. Arrival
a. They like a very slim look, sexy looking and inviting to use
2. Engagement
a. We anticipate that the wait staff will do a brief “how to” at the time of greeting.
3. Experience
a. Create lots of guest interaction and ease of use
b. Guests need to be able to contact server…i.e. pager, central communications
i. Make simple requests…i.e. another round, want to place new order, need check, please take my payment

1. Menu – please see images.
a. As you can see there are multiple categories with this. We have the top category that shows all the different menu sub-categories i.e. Appetizers, Entrees etc. This needs to support as many of these subs as needed. Some restaurants have only a few and others have 15 to 20
b. First Sub-category would be from the list mentioned above. Supporting as many dish choices as needed. This needs to support static images or photos with a brief description of the food item.
c. Second sub-category would be to highlight a selected item. Multiple photos or video supported as well as full disclosure including nutritional info.
2. A search for allergenic or specific ingredients is needed.
3. Help me decide. A filter to help pin point a food or drink item from a list of a few questions.
It is important to note that the restaurant menu is the function that over laps the ad windows. This can be a full page view.

Front Interface should look like this
1. 3 ad windows 1 - 728x90 bottom and 2 300X250
2. Tool bar should have menu front and center
a. Food menu – Launches video and opens menu
b. Drink menu – Launches video and opens menu with build your own cocktail
c. Promotions – mostly video content for food and drink items
3. The remaining features
a. Table Chat
b. Entertainment i.e. websites, Linkora, chirpex and 9 pt
c. Games
d. Photo share
e. Contest
f. Reviews
g. Call staff

```html
<!DOCTYPE html>
<html lang="en">
<head>
<meta charset="utf-8">
<title>Brevlo – Tavla Menu Interface</title>
<link href="https://fonts.googleapis.com/css2?family=Ubuntu:wght@400;500;700&family=PT+Serif&family=Oswald:wght@600;700&display=swap" rel="stylesheet">
<style>
:root{
  --stage:#1b1612;
  --bar:#0b0b0b;
  --wood-1:#c9945c;
  --wood-2:#a8733f;
  --wood-3:#b98450;
  --tab-brown:#9a6a3c;
  --tab-brown-dark:#7d532c;
  --paper:#f3f1ed;
  --paper-shade:#e4e1dc;
  --red:#d0201c;
  --red-dark:#a8150f;
  --gray-band:#7d7b76;
  --gray-chip:#5f5d58;
  --side:#4a4640;
  --side-dark:#37332e;
  --bottom:#6e6b63;
  --text-dark:#3a3a3a;
  --text-light:#f4f4f4;
  --social:#1f6fb3;
  --banner-blue:#1c3f8c;
  --brand-pink:#d81b6a;
}
*{box-sizing:border-box;margin:0;padding:0}
html,body{width:1200px;height:840px;overflow:hidden;background:var(--stage);font-family:"Ubuntu",sans-serif}
.screen{position:absolute;left:48px;top:8px;width:1104px;height:824px;background:var(--bottom);overflow:hidden}
.status-bar{position:absolute;left:0;top:0;width:100%;height:18px;background:var(--bar);color:#ddd;font-size:11px;display:flex;align-items:center;justify-content:space-between;padding:0 10px}
.status-bar .battery{width:22px;height:9px;border:1px solid #ddd;border-radius:2px;position:relative}
.status-bar .battery::after{content:"";position:absolute;inset:1px 3px 1px 1px;background:#ddd}
/* left wood panel */
.menu-panel{position:absolute;left:0;top:18px;width:781px;height:688px;
  background:repeating-linear-gradient(90deg,var(--wood-1) 0 38px,var(--wood-3) 38px 41px,var(--wood-2) 41px 44px,var(--wood-1) 44px 90px);}
.company-logo{position:absolute;left:38px;top:27px;color:#4a3520;font-size:19px;line-height:24px}
.tab{position:absolute;top:43px;height:56px;border-radius:6px 6px 0 0;font-size:21px;display:flex;align-items:center;justify-content:center;color:var(--text-light);background:linear-gradient(var(--tab-brown),var(--tab-brown-dark))}
.tab.is-active{background:var(--paper);color:var(--red);height:62px}
.tab-food{left:202px;width:164px}
.tab-drink{left:385px;width:175px}
.tab-promo{left:553px;width:176px}
.menu-card{position:absolute;left:22px;top:94px;width:738px;height:572px;background:linear-gradient(135deg,var(--paper),var(--paper-shade) 45%,var(--paper) 70%,var(--paper-shade));box-shadow:0 3px 6px rgba(0,0,0,.35),6px 6px 0 -1px #ece9e4,7px 8px 6px rgba(0,0,0,.25)}
.hero-photo{position:absolute;left:4px;top:26px;width:730px;height:211px;background:radial-gradient(ellipse at 40% 45%,#5a2c1c 0,#3b1c12 22%,#9a8a80 48%,#e9e6e2 75%)}
.category-bar{position:absolute;left:4px;top:238px;width:730px;height:45px;background:linear-gradient(#9c9a95,var(--gray-band));display:flex;align-items:center;gap:9px;padding-left:12px}
.category{width:108px;height:33px;border-radius:3px;background:var(--gray-chip);color:#eee;font-size:14px;display:flex;align-items:center;justify-content:center}
.category.is-faded{opacity:.35}
.category.is-active{background:var(--red);position:relative}
.category.is-active::after{content:"";position:absolute;bottom:-8px;left:50%;margin-left:-8px;border:8px solid transparent;border-bottom:0;border-top-color:var(--red)}
.pager{position:absolute;top:362px;width:26px;height:40px}
.dish{position:absolute;top:312px;width:290px}
.dish-photo{position:absolute;left:0;top:0;width:103px;height:97px;border:3px solid #fff;box-shadow:0 1px 3px rgba(0,0,0,.4)}
.dish-price{position:absolute;left:14px;bottom:6px;background:#222;color:#fff;font-size:13px;font-weight:700;padding:3px 10px;border-radius:3px}
.dish-name{position:absolute;left:119px;top:6px;width:175px;color:var(--red);font-size:13.5px;line-height:17px;text-transform:uppercase}
.dish-desc{position:absolute;left:119px;top:66px;width:165px;color:var(--text-dark);font-size:12px;line-height:16px}
.dish-one{left:72px}.dish-two{left:387px}
.btn{position:absolute;top:502px;height:45px;border-radius:5px;color:#fff;font-size:16px;display:flex;align-items:center;justify-content:center;gap:10px}
.btn-chat{left:230px;width:238px;background:linear-gradient(#8e8c86,#666460)}
.btn-decide{left:486px;width:212px;background:linear-gradient(#e12b24,var(--red-dark));clip-path:polygon(0 0,92% 0,100% 50%,92% 100%,0 100%)}
/* sidebar */
.sidebar{position:absolute;left:781px;top:18px;width:323px;height:688px;background:linear-gradient(var(--side),var(--side-dark) 25%)}
.search{position:absolute;left:23px;top:16px;width:212px;height:43px;background:#5c5852;border-radius:4px 0 0 4px;color:#eee;font-size:14px;display:flex;align-items:center;padding-left:18px;box-shadow:inset 0 1px 3px rgba(0,0,0,.5)}
.search-btn{position:absolute;left:235px;top:16px;width:65px;height:43px;background:var(--red);clip-path:polygon(0 0,80% 0,100% 50%,80% 100%,0 100%)}
.social{position:absolute;top:75px;width:46px;height:46px;background:var(--social);border-radius:3px;color:#fff;font-size:9px;display:flex;align-items:center;justify-content:center}
.social-a{left:75px}.social-b{left:141px}.social-c{left:206px}
.ad-square{position:absolute;left:0;width:323px;height:270px}
.ad-recipes{top:143px;background:#fff}
.ad-recipes .ad-photo{position:absolute;inset:0 0 62px 0;background:radial-gradient(circle at 55% 40%,#e76a2c,#c5401a 55%,#f0e0d0)}
.ad-recipes .headline{position:absolute;left:4px;top:58px;background:#fff;font-family:"PT Serif",serif;font-size:24px;padding:0 6px}
.ad-recipes .tagline{position:absolute;left:8px;top:212px;font-family:"PT Serif",serif;font-size:18px;line-height:22px}
.ad-recipes .brand{position:absolute;right:8px;top:234px;font-family:"PT Serif",serif;font-size:26px;line-height:30px;color:var(--brand-pink)}
.ad-news{top:417px;background:#8fb6c8}
.ad-news .ad-photo{position:absolute;inset:0 0 70px 0;background:linear-gradient(#5d8fbf,#cfd9e4 42%,#6f7a70 60%,#b5742e 80%,#4e5a2a)}
.ad-news .masthead{position:absolute;left:0;right:0;bottom:8px;text-align:center;color:#fff;font-family:"Oswald",sans-serif}
.ad-news .masthead b{display:block;font-size:28px;line-height:30px}
.ad-news .masthead span{font-size:14px;letter-spacing:3px}
/* bottom ad */
.ad-banner{position:absolute;left:162px;top:716px;width:787px;height:97px;background:#fff;overflow:hidden}
.ad-banner .art{position:absolute;left:0;top:0;width:338px;height:97px;background:linear-gradient(90deg,#223a6e,#e8e8ee 40%,#2b3f78 70%,#fff)}
.ad-banner .slogan{position:absolute;left:346px;top:8px;font-family:"Oswald",sans-serif;font-weight:700;font-size:31px;line-height:29px;color:var(--banner-blue)}
.ad-banner .slogan em{font-style:normal;color:var(--red)}
.ad-banner .pledge{position:absolute;left:346px;top:66px;font-size:18px;color:#111}
.ad-banner .badge{position:absolute;left:600px;top:14px;width:170px;height:68px;border:3px solid var(--banner-blue);border-radius:8px}
</style>
</head>
<body>
<main class="screen">
  <div class="status-bar"><span>Tavla</span><span>4:20 PM</span><span class="battery"></span></div>

  <section class="menu-panel">
    <div class="company-logo">Company<br>logo here</div>
    <div class="tab tab-drink">Drink Menu</div>
    <div class="tab tab-promo">Promotions</div>
    <div class="menu-card">
      <div class="hero-photo" role="img" aria-label="Plated grilled steak with sauce and vegetables"></div>
      <nav class="category-bar">
        <span class="category is-faded">Appetizers</span>
        <span class="category is-active">Entrees</span>
        <span class="category">Desserts</span>
        <span class="category">Soups</span>
        <span class="category">Appetizers</span>
        <span class="category">Entrees</span>
      </nav>
      <svg class="pager" style="left:8px" viewBox="0 0 26 40"><path d="M20 4 6 20l14 16" fill="none" stroke="#999" stroke-width="3"/></svg>
      <svg class="pager" style="left:704px" viewBox="0 0 26 40"><path d="M6 4l14 16L6 36" fill="none" stroke="#999" stroke-width="3"/></svg>
      <article class="dish dish-one">
        <div class="dish-photo" role="img" aria-label="Grilled fish with lobster sauce" style="background:radial-gradient(circle,#d7502a,#7a3a1c)"><span class="dish-price">$11.90</span></div>
        <h3 class="dish-name">Pan-grilled catch of the day with lobster sauce</h3>
        <p class="dish-desc">Pan-grilled catch of the day prepared with home-made lobster sauce. Served with french fries.</p>
      </article>
      <article class="dish dish-two">
        <div class="dish-photo" role="img" aria-label="Penne pasta with turkey ham and cheese" style="background:radial-gradient(circle,#e39a4a,#9a4f22)"><span class="dish-price">$10.90</span></div>
        <h3 class="dish-name">Penne with turkey ham and cheese</h3>
        <p class="dish-desc" style="top:46px">Penne pasta with tomato and turkey ham topped with loads of mozzarella cheese.</p>
      </article>
      <div class="btn btn-chat">
        <svg width="22" height="18" viewBox="0 0 22 18"><ellipse cx="9" cy="8" rx="8" ry="6" fill="#444"/><ellipse cx="14" cy="10" rx="7" ry="5" fill="#999"/></svg>
        Chat With the Staff</div>
      <div class="btn btn-decide">Help Me Decide <span style="color:#ff8a80;font-size:22px">?</span></div>
    </div>
    <div class="tab tab-food is-active">Food Menu</div>
  </section>

  <aside class="sidebar">
    <div class="search">Ingredient Search</div>
    <div class="search-btn">
      <svg width="52" height="43" viewBox="0 0 52 43"><circle cx="24" cy="19" r="8" fill="none" stroke="#fff" stroke-width="3"/><path d="M30 25l7 7" stroke="#fff" stroke-width="3"/></svg>
    </div>
    <div class="social social-a">Linkora</div>
    <div class="social social-b">Chirpex</div>
    <div class="social social-c">nine pt</div>

    <div class="ad-square ad-recipes">
      <div class="ad-photo" role="img" aria-label="Forkful of spaghetti in tomato sauce"></div>
      <div class="headline">Impress him</div>
      <div class="tagline">Free easy recipes from</div>
      <div class="brand">DishNote</div>
    </div>
    <div class="ad-square ad-news">
      <div class="ad-photo" role="img" aria-label="Snowy mountain range above autumn forest"></div>
      <div class="masthead"><b>RIDGELINE</b><span>WEEKLY NEWS</span></div>
    </div>
  </aside>

  <div class="ad-banner">
    <div class="art" role="img" aria-label="Illustrated figure in red, white and blue"></div>
    <div class="slogan">KEEP IT IN THE<br><em>LOOP FOR</em> GOOD</div>
    <div class="pledge">Sort your bins every week.</div>
    <div class="badge"></div>
  </div>
</main>
</body>
</html>
```